Two Web Pages Design for an Anti-Aging Med Spa

Hi,
We are looking to redesign our website which is an Medspa in the Anti-Aging and Hormone Replacement business. We only need two pages designed. Frontpage and one inner page. and we need professional clean looks with matching colors to our logo (see attached files).
Sites we like:
http://velmorabeauty.example/
http://www.brindlequartz.example/

Target Market(s)

Mid-Age Men and Women

Industry/Entity Type

Business

Number of Pages Required

2 page

Font styles to use
Sans Serif

Colors
86cfc6
33b7a4
33a6d7
85cae6
ffffff
cadf82
9bcb3b
fde08a

Requirements
Must have
• IMPORTANT: YOU WOULD ONLY NEED TO DESIGN THE FRONTPAGE AND ONE INNER PAGE, NOT THE WHOLE SITE. FRONT-PAGE MUST INCLUDE A SLIDER. If you have any other questions please PM me.

```html
<!DOCTYPE html>
<html lang="en">
<head>
<meta charset="utf-8">
<title>Evermore Vital – Anti-Aging Med Spa</title>
<link href="https://fonts.googleapis.com/css2?family=Open+Sans:ital,wdth,wght@0,75..100,300..800;1,75..100,300..800&display=swap" rel="stylesheet">
<style>
:root{
  --teal:#33b7a4;
  --teal-soft:#86cfc6;
  --blue:#33a6d7;
  --sky:#85cae6;
  --lime:#9bcb3b;
  --lime-soft:#cadf82;
  --butter:#fde08a;
  --white:#ffffff;
  --ink:#3a3a3a;
  --muted:#8a8a8a;
  --panel:#f4f3f4;
  --earth:#574845;
  --footer-text:#e8e2df;
}
*{box-sizing:border-box;margin:0;padding:0}
html,body{width:1200px;height:2786px;overflow:hidden}
body{position:relative;font-family:"Open Sans",Arial,sans-serif;color:var(--ink);background:var(--white)}
.abs{position:absolute}

.topbar{left:0;top:0;width:1200px;height:47px;background:var(--teal);color:var(--white)}
.topbar .links{left:128px;top:14px;font-size:12px;letter-spacing:.3px}
.topbar .call{left:735px;top:11px;font-size:17px;font-weight:700}
.topbar .call span{font-weight:400}
.topbar .social{left:955px;top:9px;display:flex;gap:6px}
.topbar .social i{display:block;width:27px;height:27px;border:2px solid var(--white);border-radius:50%}

.header{left:0;top:47px;width:1200px;height:107px;background:var(--white)}
.brand{left:128px;top:40px;display:flex;align-items:center;gap:8px;font-size:19px;font-weight:700;color:var(--teal)}
.brand i{display:block;width:18px;height:18px;border-radius:50%;background:var(--lime)}
.nav{left:408px;top:55px;display:flex;gap:34px;font-size:12px;font-weight:600;text-transform:uppercase}

.hero{left:0;top:154px;width:1200px;height:532px;background:linear-gradient(100deg,#4a3b33 0%,#a38f7c 30%,#e6e1da 55%,#c9c2b8 80%,#f1efec 100%)}
.hero-badge{left:128px;top:321px;width:365px;height:168px;background:var(--lime);color:var(--white);padding:26px 22px}
.hero-badge h1{font-weight:300;font-stretch:75%;font-size:64px;line-height:1;letter-spacing:1px}
.hero-badge p{font-size:16px;margin-top:12px;white-space:nowrap;font-stretch:90%}
.dots{display:flex;gap:8px}
.dots i{display:block;width:14px;height:14px;border-radius:50%;background:#bbb}
.dots i.on{background:var(--lime)}

.service{height:154px;border-radius:77px 0 0 77px;display:flex;align-items:center}
.service .ring{width:154px;height:154px;border-radius:50%;border:8px solid var(--white);flex:none}
.service h3{font-size:13px;font-weight:700;font-stretch:85%;color:var(--ink);margin-bottom:10px;white-space:nowrap}
.service li{list-style:none;font-size:11px;line-height:22px;color:var(--ink);white-space:nowrap}
.service .txt{padding-left:14px}

.prompt{left:0;top:943px;width:1200px;height:214px;background:#f3f3f3;text-align:center}
.prompt h2{margin-top:50px;font-size:34px;font-weight:400;color:#222}
.prompt p{margin-top:6px;font-size:18px;color:var(--muted)}
.btn-find{display:inline-block;margin-top:18px;width:215px;height:37px;line-height:37px;background:var(--teal-soft);color:var(--white);font-size:17px}

.sec-title{font-size:25px;font-weight:400}
.regen-photo{left:128px;top:1286px;width:193px;height:178px;border:1px solid #ddd;padding:10px}
.regen-photo div{width:100%;height:100%;background:linear-gradient(135deg,#f2e3da,#c9a58f)}
.regen-text{left:341px;top:1282px;width:225px;font-size:13px;line-height:20px;color:var(--muted)}
.btn-brochure{left:341px;top:1425px;width:205px;height:41px;background:var(--lime);color:var(--white);font-size:14px;display:flex;align-items:center;gap:10px;padding-left:12px}
.quote{left:654px;top:1286px;width:417px;height:107px;background:#f3f3f3;padding:14px 16px 0 120px;font-size:13px;font-style:italic;line-height:19px;color:#555}
.avatar{left:676px;top:1296px;width:96px;height:96px;border-radius:50%;border:4px solid var(--white);background:linear-gradient(#3a3a3a,#d9b9a2)}
.quote-name{left:788px;top:1428px;font-size:15px;color:var(--blue)}

.blog{left:0;top:1528px;width:1200px;height:696px;background:var(--sky)}
.card{top:1646px;width:275px;height:461px;background:var(--white)}
.card .img{height:176px}
.card h4{margin:36px 14px 12px;font-size:15px;font-weight:700;color:#333}
.card p{margin:0 14px;font-size:13px;line-height:21px;color:#666}
.card .meta{position:absolute;left:0;bottom:0;width:100%;height:40px;background:#f5f5f5;display:flex;align-items:center;justify-content:space-between;padding:0 14px;font-size:11px;color:#555}
.card .meta span{display:flex;align-items:center;gap:8px}

.register{left:0;top:2229px;width:1200px;height:171px;background:var(--panel)}
.register h5{position:absolute;left:128px;top:70px;font-size:19px;font-weight:400;color:#555}
.field{top:2293px;height:39px;background:var(--white);font-size:13px;color:#999;padding:11px 12px}
.btn-submit{left:945px;top:2293px;width:126px;height:39px;background:var(--lime);color:var(--white);font-size:15px;text-align:center;line-height:39px}

.footer{left:0;top:2400px;width:1200px;height:335px;background:var(--earth)}
.fcol{top:2448px;font-size:13px;color:var(--footer-text)}
.fcol h6{font-size:15px;font-weight:700;color:var(--white);margin-bottom:26px;white-space:nowrap}
.fcol li{list-style:none;border-bottom:1px dashed #8a7c78;padding:6px 0 10px;width:170px;font-size:12px;white-space:nowrap}
.fcol small{display:flex;gap:6px;align-items:center;margin-top:4px;font-size:12px;color:#cfc6c2}
.bottombar{left:0;top:2735px;width:1200px;height:51px;background:var(--teal);color:var(--white);font-size:12px}
</style>
</head>
<body>

<div class="abs topbar">
  <div class="abs links">SHOP &nbsp;| &nbsp;TESTIMONIALS &nbsp;| &nbsp;NEWSLETTER SIGNUP &nbsp;| &nbsp;CONTACT US</div>
  <div class="abs call">CALL NOW! <span>555-014-2290</span></div>
  <div class="abs social"><i></i><i></i><i></i><i></i></div>
</div>

<div class="abs header">
  <div class="abs brand"><i></i>EVERMORE VITAL</div>
  <nav class="abs nav"><span>Home</span><span>About Us</span><span>Hormone Replacement ▾</span><span>Rejuvenation ▾</span><span>Weight and Health ▾</span><span>Blog</span></nav>
</div>

<div class="abs hero" role="img" aria-label="Bright treatment room with a white reclining spa chair and skincare posters on the wall"></div>
<div class="abs hero-badge"><h1>BACK TO LIFE</h1><p>Natural therapies to feel like yourself again</p></div>
<div class="abs dots" style="left:570px;top:636px"><i></i><i class="on"></i><i></i></div>

<div class="abs service" style="left:128px;top:729px;width:305px;background:var(--butter)">
  <div class="ring" role="img" aria-label="Couple embracing outdoors" style="background:linear-gradient(#c9d7e4,#b07f65)"></div>
  <div class="txt"><h3>Hormone Replacement</h3><ul><li>BHRT for Women</li><li>BHRT for Men</li></ul></div>
</div>
<div class="abs service" style="left:446px;top:729px;width:305px;background:var(--lime-soft)">
  <div class="ring" role="img" aria-label="Woman with smooth skin" style="background:linear-gradient(#f3e8dc,#d8b59c)"></div>
  <div class="txt"><h3>Rejuvenation</h3><ul><li>Platelet Rich Plasma Therapy</li><li>Smoothara</li><li>Fillers</li></ul></div>
</div>
<div class="abs service" style="left:767px;top:729px;width:305px;background:var(--sky)">
  <div class="ring" role="img" aria-label="Woman stretching in a yoga pose" style="background:linear-gradient(#eaf4fa,#9ccbe3)"></div>
  <div class="txt"><h3>Weight and Health</h3><ul><li>hCG Diet</li><li>Meal Plans/Fitness</li><li>Vitamin Bar</li></ul></div>
</div>

<div class="abs prompt">
  <h2>WANT TO UNDERSTAND WHY YOU ARE SLUGGISH?</h2>
  <p>Lets us help you get back to feeling like yourself</p>
  <span class="btn-find">Find out more...</span>
</div>

<h3 class="abs sec-title" style="left:128px;top:1214px;color:var(--lime)">REAL REGENERATION</h3>
<div class="abs regen-photo"><div role="img" aria-label="Woman relaxing during a facial treatment"></div></div>
<p class="abs regen-text">Did you know Skin Regeneration Therapy, a type of regenerative therapy with the patient's own blood, uses components called Platelets in the blood to rejuvenate the body from within?</p>
<div class="abs btn-brochure">
  <svg width="20" height="22" viewBox="0 0 20 22"><rect x="2" y="1" width="16" height="20" fill="none" stroke="#fff" stroke-width="2"/><path d="M6 8h8M6 12h8M6 16h5" stroke="#fff" stroke-width="2"/></svg>
  Download our brochure
</div>

<h3 class="abs sec-title" style="left:654px;top:1214px;color:var(--blue)">WHAT ARE PATIENTS SAY</h3>
<div class="abs quote">Lorem ipsum dar sit amet, consectetur adipiscing elit. Fusce pellentesque lorem sed tortor dignissim commodo. Duis tem por malesuada dignissim. Donec quis ma gna mauris.</div>
<div class="abs avatar" role="img" aria-label="Portrait of a patient"></div>
<div class="abs quote-name">Nora Vale</div>
<div class="abs dots" style="left:1018px;top:1442px"><i></i><i style="background:var(--blue)"></i><i></i></div>

<div class="abs blog"><h3 class="sec-title" style="position:absolute;left:128px;top:50px;color:var(--white)">FROM THE BLOG</h3></div>

<div class="abs card" style="left:128px">
  <div class="img" role="img" aria-label="Senior couple laughing on a beach" style="background:linear-gradient(#9fb9c9,#d6b48d)"></div>
  <h4>PUT THE HEADING HERE</h4>
  <p>Lorem ipsum dolor sit amet, consectetur adipiscing elit, sed do eiusmod tempor incididunt ut labore et dolore magna aliqua. Lorem ipsum dolor sit amet, con sectetur adipiscing elit, sed do eiusmod tempor. Sed do eiusmod tempor</p>
  <div class="meta"><span>▦ December 22, 2014</span><span>● 3 comments</span></div>
</div>
<div class="abs card" style="left:463px">
  <div class="img" role="img" aria-label="Smiling woman with long brown hair" style="background:linear-gradient(#d9cfc8,#7a5642)"></div>
  <h4>PUT THE HEADING HERE</h4>
  <p>Lorem ipsum dolor sit amet, consectetur adipiscing elit, sed do eiusmod tempor incididunt ut labore et dolore magna aliqua. Lorem ipsum dolor sit amet, con sectetur adipiscing elit, sed do eiusmod tempor. Sed do eiusmod tempor</p>
  <div class="meta"><span>▦ December 22, 2014</span><span>● 3 comments</span></div>
</div>
<div class="abs card" style="left:797px">
  <div class="img" role="img" aria-label="Man jogging along the shoreline" style="background:linear-gradient(#bfe0ee,#5fa9c4 60%,#e8dcc8)"></div>
  <h4>PUT THE HEADING HERE</h4>
  <p>Lorem ipsum dolor sit amet, consectetur adipiscing elit, sed do eiusmod tempor incididunt ut labore et dolore magna aliqua. Lorem ipsum dolor sit amet, con sectetur adipiscing elit, sed do eiusmod tempor. Sed do eiusmod tempor</p>
  <div class="meta"><span>▦ December 22, 2014</span><span>● 3 comments</span></div>
</div>

<div class="abs register"><h5>REGISTER TODAY FOR OUR UPCOMING OFFERS</h5></div>
<div class="abs field" style="left:557px;width:182px">Name</div>
<div class="abs field" style="left:750px;width:188px">Email</div>
<div class="abs btn-submit">Submit</div>

<div class="abs footer"></div>
<div class="abs fcol" style="left:128px;width:200px">
  <h6>ABOUT EVERMORE VITAL</h6>
  <p style="line-height:22px">We are medical practice dedicated to improving the quality of life for men and women naturally through bio-identical hormone replacement therapy (HRT), nutrition and exercise</p>
  <div style="margin-top:16px;margin-left:30px;font-weight:700;color:var(--teal)">EVERMORE VITAL</div>
</div>
<div class="abs fcol" style="left:403px">
  <h6>RECENT STUDIES</h6>
  <ul><li>Hormonal Changes in Men<small>▦ June, 2014</small></li><li>PRP Therapy in Ortho<small>▦ February, 2014</small></li><li>hCG Diet Study<small>▦ February, 2014</small></li></ul>
</div>
<div class="abs fcol" style="left:626px">
  <h6>EASY LINKS</h6>
  <ul><li>World Health</li><li>Anti Aging Institute</li><li>Renew Platelet Lab</li><li>Smoothara Cosmetic</li></ul>
</div>
<div class="abs fcol" style="left:853px">
  <h6>CONNECT US WITH</h6>
  <p>Signup for our Newsletter</p>
  <div style="margin-top:26px;display:flex"><div style="width:171px;height:35px;background:#fff;color:#999;font-size:11px;padding:10px">Email</div><div style="width:47px;height:35px;background:var(--lime);color:#fff;text-align:center;line-height:35px;font-weight:700">›</div></div>
  <div style="margin-top:30px;margin-left:36px;display:flex;gap:8px">
    <i style="width:39px;height:39px;border-radius:50%;background:#4fb7e8;display:block"></i>
    <i style="width:39px;height:39px;border-radius:50%;background:#4a8fc1;display:block"></i>
    <i style="width:39px;height:39px;border-radius:50%;background:#4a67a8;display:block"></i>
    <i style="width:39px;height:39px;border-radius:50%;background:#d24b3f;display:block"></i>
  </div>
</div>

<div class="abs bottombar">
  <span class="abs" style="left:128px;top:18px">Home | About Us | Hormone Replacement | Rejuvenation | Weight and Health | Blog</span>
  <span class="abs" style="left:928px;top:18px">Copyright © 2015 EVERMORE VITAL</span>
</div>

</body>
</html>
```